Make it cool to work near where you are...

Calling all creatives - create the ultimate cool card for people who want to cut their commute.

Here at TilloPod we've got what can best be described as an Marlin pass for desks - and we want to brighten up the wallets of our most loyal users.

So, pitch us your ideas and you might see your design on cards being flashed across the country - and we've thrown in a bit of cash too.

Do see our brief card guidelines - with a couple of past examples thrown in.

Industry/Entity Type

Cash

```html
<!DOCTYPE html>
<html lang="en">
<head>
<meta charset="utf-8">
<title>TilloPod Marlin pass card</title>
<link href="https://fonts.googleapis.com/css2?family=Quicksand:wght@400;600&display=swap" rel="stylesheet">
<style>
  :root {
    --page-bg: #ecebea;
    --card-dark: #3a3536;
    --strip-white: rgba(240, 240, 242, 0.88);
    --number-navy: #2e3560;
    --url-grey: #d6d3d3;
    --brand-white: #ffffff;
    --pattern-orange: #d98a45;
    --pattern-rust: #a8553a;
    --pattern-grey: #b9b9bb;
    --pattern-black: #2a2424;
    --pattern-cream: #ead8c4;
  }
  html, body {
    margin: 0;
    width: 1200px;
    height: 782px;
    overflow: hidden;
    background: var(--page-bg);
  }
  .canvas {
    position: relative;
    width: 1200px;
    height: 782px;
  }
  .member-card {
    position: absolute;
    left: 172px;
    top: 121px;
    width: 856px;
    height: 540px;
    border-radius: 24px;
    overflow: hidden;
    background: var(--card-dark);
    font-family: "Quicksand", sans-serif;
  }
  .card-pattern {
    position: absolute;
    left: 0;
    top: 0;
    width: 856px;
    height: 427px;
    background:
      linear-gradient(160deg, transparent 0 30%, rgba(42,36,36,0.55) 30% 42%, transparent 42%),
      linear-gradient(20deg, var(--pattern-grey) 0%, var(--pattern-orange) 28%, var(--pattern-rust) 45%, var(--pattern-cream) 58%, var(--pattern-orange) 72%, var(--pattern-grey) 100%);
  }
  .number-strip {
    position: absolute;
    left: 0;
    top: 302px;
    width: 856px;
    height: 43px;
    background: var(--strip-white);
  }
  .card-number {
    position: absolute;
    left: 82px;
    top: 300px;
    font-size: 31px;
    line-height: 46px;
    letter-spacing: 3px;
    color: var(--number-navy);
    font-weight: 400;
  }
  .bottom-band {
    position: absolute;
    left: 0;
    top: 427px;
    width: 856px;
    height: 113px;
    background: var(--card-dark);
  }
  .brand-name {
    position: absolute;
    left: 600px;
    top: 392px;
    width: 220px;
    text-align: center;
    font-size: 34px;
    line-height: 48px;
    font-weight: 600;
    color: var(--brand-white);
  }
  .card-url {
    position: absolute;
    left: 0;
    top: 464px;
    width: 820px;
    text-align: center;
    font-size: 20px;
    line-height: 30px;
    letter-spacing: 3.5px;
    color: var(--url-grey);
    font-weight: 400;
  }
</style>
</head>
<body>
  <main class="canvas">
    <section class="member-card" aria-label="TilloPod Marlin pass">
      <div class="card-pattern" role="img" aria-label="Low-poly geometric pattern in orange, rust, grey, cream and black facets"></div>
      <div class="number-strip"></div>
      <p class="card-number" style="margin:0">777777777777</p>
      <div class="bottom-band"></div>
      <p class="brand-name" style="margin:0">TilloPod</p>
      <p class="card-url" style="margin:0">www.tillopod.com/card</p>
    </section>
  </main>
</body>
</html>
```